ZEPRILO.COM is a premium domain sales company. Our competitors are companies like vastplots.example, getparcels.example, peerwords.example. Our current site is at www.zeprilos.example.

We want to have the ability to search for domains, to highlight special offers and have some testimonials on the index page.

The logo for the site is attached.

Please be sure that the order form fits on the screen without scrolling the page. I want the entire form, including the submit button to fit without any page scrolling.

Delivered product - INDEX PAGE, ORDER FORM AND CONTENT PAGE PSDs.

Target Market(s)

Small to Medium business professionals

Industry/Entity Type

It Company

Requirements
Must have
• 1. List of domains for sale
2. Simple search box with button to run the search
3. link for advanced search
4. testimonial area. Note - this can be a small box where a different testimonial is displayed on each page load.
Nice to have
• Would like the site to have some white space. Don't want a heavily packed website. Give it an "airy" feel.

```html
<!DOCTYPE html>
<html lang="en">
<head>
<meta charset="utf-8">
<title>ZEPRILO.COM – Premium Domains</title>
<link rel="stylesheet" href="https://fonts.googleapis.com/css2?family=Arimo:ital,wght@0,400;0,700;1,400&family=Open+Sans:wght@400;600&display=swap">
<style>
:root{
  --blue-deep:#1d5d9c;
  --blue-mid:#3a7ab8;
  --blue-light:#6fa3d4;
  --blue-text:#0f4f8a;
  --nav-active:#0d4f96;
  --green:#2f8a2f;
  --green-btn:#3c9b25;
  --grey-btn:#b9b9b9;
  --row-alt:#efefef;
  --text:#555;
  --text-dark:#333;
  --panel:#e4e4e4;
  --footer:#c8c8c8;
  --footer-text:#1f5f9e;
  --white:#fff;
}
*{box-sizing:border-box;margin:0;padding:0}
html,body{width:1200px;height:1055px;overflow:hidden;background:var(--white);font-family:"Arimo",Arial,sans-serif}
.page{position:relative;width:1200px;height:1055px}
.abs{position:absolute}

/* header */
.hero{left:0;top:0;width:1200px;height:404px;overflow:hidden;
  background:
   radial-gradient(ellipse 420px 260px at 330px 40px,rgba(190,215,240,.75),rgba(190,215,240,0) 70%),
   linear-gradient(180deg,#3f7fbd 0%,#2a6aab 55%,#1f5c9b 100%);}
.hero-beams{left:0;top:0}
.brand{left:190px;top:30px;display:flex;align-items:center;gap:10px;color:var(--white);font-weight:700;font-size:40px;letter-spacing:.5px}
.brand-dot{width:22px;height:22px;border-radius:50%;background:var(--white)}
.nav{left:0;top:34px;height:34px;width:1200px}
.nav a{position:absolute;top:0;height:34px;line-height:34px;color:var(--white);text-decoration:none;font-size:21px}
.nav .active{background:var(--nav-active);padding:0 17px}
.nav-divider{position:absolute;top:6px;width:1px;height:26px;background:rgba(255,255,255,.35)}

.hero-title{left:173px;top:128px;color:var(--white);font-size:28px}
.hero-sub{left:173px;top:175px;color:var(--white);font-size:17.5px;letter-spacing:.3px}
.search{left:172px;top:207px;width:365px;height:46px;display:flex;border-radius:6px;box-shadow:0 1px 3px rgba(0,0,0,.4)}
.search-input{flex:1;background:var(--white);border:2px solid #9a9a9a;border-right:none;border-radius:6px 0 0 6px;font-size:16px;color:#aaa;padding:0 14px;line-height:42px}
.search-btn{width:55px;background:linear-gradient(#f6f6f6,#d6d6d6);border:2px solid #6d6d6d;border-radius:0 6px 6px 0;display:flex;align-items:center;justify-content:center}
.adv-link{left:182px;top:345px;color:var(--white);font-size:20px;display:flex;align-items:center;gap:6px}
.adv-link span{border-bottom:2px dashed #9cc4ea;padding-bottom:1px}

.testi-title{left:676px;top:136px;color:#0a3f73;font-family:"Open Sans",Arial,sans-serif;font-size:32px}
.testi-sub{left:677px;top:181px;color:var(--white);font-size:16px}
.testi-source{right:186px;top:224px;color:var(--blue-text);font-weight:700;font-size:15px}
.testi-body{left:680px;top:247px;width:336px;color:var(--blue-text);font-size:14px;line-height:17.5px}
.testi-body b{font-weight:700}
.testi-date{right:186px;top:318px;color:var(--blue-text);font-weight:700;font-size:15px}
.hero-dots{left:812px;top:370px;display:flex;gap:8px}
.hero-dots i{width:12px;height:12px;border-radius:50%;background:#1b64b3;box-shadow:inset 0 1px 2px rgba(0,0,0,.4)}
.hero-dots i.on{background:#dfe6ee}

/* premium table */
.section-title{color:var(--green);font-size:22px}
.premium-title{left:168px;top:413px}
.domain-table{left:166px;top:446px;width:611px;border-top:1px solid #ddd;border-bottom:2px solid #ccc;border-collapse:collapse}
.domain-table th{height:35px;font-weight:400;font-size:16px;color:var(--text-dark);text-align:center}
.domain-table th:first-child{text-align:left;padding-left:10px}
.domain-table td{height:41.7px;color:#666;font-size:15px;text-align:center}
.domain-table tbody tr:nth-child(odd){background:var(--row-alt)}
.domain-table td.name{text-align:left;padding-left:10px;font-size:19px;color:#555}
.domain-table td.name small{font-size:15px;color:#777}
.buy{display:inline-block;width:53px;height:24px;line-height:24px;border-radius:12px;background:var(--grey-btn);color:var(--white);font-weight:700;font-size:12px;letter-spacing:.5px}
.buy.on{background:var(--green-btn)}
.view-more{right:430px;top:793px;color:#555;font-style:italic;font-size:15px}

/* advanced search panel */
.adv-title{left:806px;top:417px}
.adv-panel{left:786px;top:445px;width:264px;height:332px;background:repeating-linear-gradient(135deg,#e6e6e6 0 3px,#e0e0e0 3px 6px);padding:14px 20px;color:var(--text-dark);font-size:19px}
.field{background:var(--white);border:2px solid #cfcfcf;border-radius:3px}
.kw-input{position:absolute;left:20px;top:54px;width:226px;height:30px}
.lbl{position:absolute;left:20px}
.check{position:absolute;top:134px;display:flex;align-items:center;gap:4px;font-size:17px}
.check i{width:18px;height:18px;background:var(--white);border:1px solid #999}
.range{position:absolute;left:95px;display:flex;align-items:center;gap:9px;font-size:18px;color:#666}
.range .field{width:58px;height:26px;border-width:1px}
.submit{position:absolute;right:12px;top:272px;width:80px;height:26px;line-height:26px;border-radius:13px;background:#8d8d8d;color:var(--white);font-weight:700;font-size:13px;text-align:center;letter-spacing:.5px}

/* quote band */
.quote-band{left:144px;top:819px;width:905px;height:95px;background:linear-gradient(90deg,#fff 0%,#e8efe8 20%,#fbfcfb 50%,#e8efe8 80%,#fff 100%)}
.corner{position:absolute;width:20px;height:20px;border-color:#666;border-style:solid}
.corner.tl{left:20px;top:5px;border-width:4px 0 0 4px}
.corner.br{right:6px;bottom:3px;border-width:0 4px 4px 0}
.quote-text{position:absolute;left:167px;top:17px;color:var(--blue-text);font-size:18px}
.quote-author{position:absolute;left:177px;top:58px;color:var(--text-dark);font-size:19px}
.stars{position:absolute;left:256px;top:57px;display:flex;gap:2px}
.quote-date{position:absolute;left:400px;top:61px;color:var(--text-dark);font-size:15px}
.quote-site{position:absolute;left:681px;top:57px;color:var(--text-dark);font-size:19px}
.band-dots{left:551px;top:929px;display:flex;gap:7px}
.band-dots i{width:11px;height:11px;background:#555}
.band-dots i.on{background:var(--white);border:2px solid var(--green-btn)}

/* footer */
.footer{left:0;top:959px;width:1200px;height:96px;background:var(--footer);text-align:center;color:var(--footer-text);font-size:15px}
.footer p{position:absolute;width:100%}
</style>
</head>
<body>
<div class="page">

  <header class="hero abs">
    <svg class="hero-beams abs" width="1200" height="404" aria-hidden="true">
      <polygon points="590,404 700,0 820,0 720,404" fill="#ffffff" opacity=".07"/>
      <polygon points="720,404 820,0 1010,0 1060,404" fill="#ffffff" opacity=".09"/>
      <polygon points="860,0 1200,0 1200,250" fill="#ffffff" opacity=".08"/>
      <polygon points="1060,404 1010,0 1200,0 1200,404" fill="#0b3f78" opacity=".12"/>
    </svg>

    <div class="brand abs"><span class="brand-dot"></span>ZEPRILO.COM</div>

    <nav class="nav abs">
      <a class="active" style="left:535px">Home</a>
      <a style="left:671px">Faqs</a>
      <span class="nav-divider" style="left:756px"></span>
      <a style="left:791px">About Us</a>
      <span class="nav-divider" style="left:931px"></span>
      <a style="left:943px">Contact</a>
    </nav>

    <h1 class="hero-title abs" style="font-weight:400">Find Perfect Your Domain Name</h1>
    <p class="hero-sub abs">You can find the best name for your business...</p>
    <div class="search abs">
      <div class="search-input">Enter Keyword Here</div>
      <div class="search-btn">
        <svg width="22" height="22" viewBox="0 0 22 22" aria-hidden="true"><circle cx="9" cy="9" r="6.5" fill="none" stroke="#333" stroke-width="2.6"/><line x1="14" y1="14" x2="20" y2="20" stroke="#333" stroke-width="3" stroke-linecap="round"/></svg>
      </div>
    </div>
    <div class="adv-link abs">
      <svg width="22" height="16" viewBox="0 0 22 16" aria-hidden="true"><path d="M1 7h4l3-5 2 1-1 4h11v2h-6v2h-1v2h-1v2H5l-4-3z" fill="none" stroke="#fff" stroke-width="1.4" stroke-linejoin="round"/></svg>
      <span>Advance Search</span>
    </div>

    <h2 class="testi-title abs" style="font-weight:400">Testimonials</h2>
    <p class="testi-sub abs">what people are saying about us...</p>
    <p class="testi-source abs">BRIGHTFOLIO.EXAMPLE</p>
    <p class="testi-body abs"><b>John:</b> Lorem Ipsum is simply dummy text of the printing and typesetting industry. Lorem Ipsum has been theindustry's standard dummy text ever since the 1500s,</p>
    <p class="testi-date abs">May 31, 2013 12:00 am</p>
    <div class="hero-dots abs"><i></i><i class="on"></i><i></i><i></i></div>
  </header>

  <h2 class="section-title premium-title abs" style="font-weight:400">Premium Domains</h2>
  <table class="domain-table abs">
    <thead><tr><th>DOMAIN</th><th>CATEGORY</th><th>PRICE</th><th>BUY NOW</th></tr></thead>
    <tbody>
      <tr><td class="name">medivora<small>.example</small></td><td>Health</td><td>$8700.00</td><td><span class="buy on">BUY</span></td></tr>
      <tr><td class="name">sportpurses<small>.example</small></td><td>Sports</td><td>$5000.00</td><td><span class="buy">BUY</span></td></tr>
      <tr><td class="name">autos-retro<small>.example</small></td><td>Vehicals</td><td>$1000.00</td><td><span class="buy">BUY</span></td></tr>
      <tr><td class="name">everyhomestead<small>.example</small></td><td>Real Estate</td><td>$999.00</td><td><span class="buy">BUY</span></td></tr>
      <tr><td class="name">daily-q<small>.example</small></td><td>Media</td><td>$197.00</td><td><span class="buy">BUY</span></td></tr>
      <tr><td class="name">plainloanrelief<small>.example</small></td><td>Finance</td><td>$300.00</td><td><span class="buy">BUY</span></td></tr>
      <tr><td class="name">Fabricaciongeneral<small>.example</small></td><td>Law</td><td>$100.00</td><td><span class="buy">BUY</span></td></tr>
    </tbody>
  </table>
  <p class="view-more abs">View more Premium Domains</p>

  <h2 class="section-title adv-title abs" style="font-weight:400">Advance Search</h2>
  <section class="adv-panel abs">
    <span class="lbl" style="top:12px">Keywords</span>
    <div class="field kw-input"></div>
    <span class="lbl" style="top:100px">Extension</span>
    <span class="check" style="left:20px"><i></i>All</span>
    <span class="check" style="left:70px"><i></i>.com</span>
    <span class="check" style="left:137px"><i></i>.org</span>
    <span class="check" style="left:196px"><i></i>.net</span>
    <span class="lbl" style="top:173px">Price</span>
    <div class="range" style="top:175px"><span class="field"></span>To<span class="field"></span></div>
    <span class="lbl" style="top:215px">Length</span>
    <div class="range" style="top:213px"><span class="field"></span>To<span class="field"></span></div>
    <div class="submit">SUBMIT</div>
  </section>

  <section class="quote-band abs">
    <span class="corner tl"></span><span class="corner br"></span>
    <p class="quote-text">“Lorem Ipsum is simply dummy text of the printing and typesetting industry.”</p>
    <p class="quote-author">Selena</p>
    <div class="stars" aria-label="5 stars">
      <svg width="112" height="22" viewBox="0 0 112 22" aria-hidden="true">
        <defs><polygon id="star" points="11,1 13.8,7.6 21,8.2 15.5,13 17.2,20.5 11,16.6 4.8,20.5 6.5,13 1,8.2 8.2,7.6" fill="#f2c21a" stroke="#c98d00" stroke-width="1"/></defs>
        <use href="#star" x="0"/><use href="#star" x="22.5"/><use href="#star" x="45"/><use href="#star" x="67.5"/><use href="#star" x="90"/>
      </svg>
    </div>
    <p class="quote-date">May 30,2013</p>
    <p class="quote-site">Clearmint.example</p>
  </section>
  <div class="band-dots abs"><i></i><i class="on"></i><i></i><i></i></div>

  <footer class="footer abs">
    <p style="top:20px">Zeprilo, Inc. 1450 Harbor Lane Suite 210&nbsp; Fairview, TN 37000&nbsp; United States ,+1 555.010.2468.</p>
    <p style="top:55px">© 2013 Zeprilo, All Right Reserved. Privacy Policy</p>
  </footer>

</div>
</body>
</html>
```